Pain Seminar Flyer 8.5x11

We are having a FREE seminar on Pain for our Bootcamp members at our gym. We are looking for a great looking flyer with pictures and a design to draw people in. I have attached our logo, pictures of the 2 speakers and a Word document of the flyer information needed. PLEASE PLEASE make our head shots small and in a circle like the example flyer we attached but obviously make the flyer much much nicer than the example. Also we attached pic ideas about pain.
- This must be in PSD. format WITH LAYERS and fonts so we can edit the time or reuse the flyer.
- Size 8.5x11
- Attached info. with pics and logo (along with other pics of pain!)
Thank you!
Gym

```html
<!DOCTYPE html>
<html lang="en">
<head>
<meta charset="utf-8">
<title>Free Seminar on How to Stop Pain</title>
<link rel="stylesheet" href="https://fonts.googleapis.com/css2?family=Open+Sans:wght@300;400;600;700;800&display=swap">
<style>
  :root {
    --blue: #2f73bb;
    --brown-dark: #5a3613;
    --brown-fold: #3d240c;
    --orange: #b8722c;
    --orange-fold: #8a5220;
    --white: #ffffff;
    --ink: #1d1d1d;
    --panel: rgba(40, 40, 40, 0.55);
    --photo-light: #cfcfcf;
    --photo-mid: #8a8a8a;
    --photo-dark: #4a4a4a;
  }
  * { margin: 0; padding: 0; box-sizing: border-box; }
  html, body { width: 855px; height: 1200px; overflow: hidden; background: #fff; }
  body { font-family: "Open Sans", Arial, sans-serif; }
  .flyer { position: relative; width: 855px; height: 1200px; overflow: hidden; }
  .hero-photo {
    position: absolute; inset: 0;
    background: radial-gradient(ellipse at 40% 55%, var(--photo-mid) 0%, var(--photo-dark) 45%, #6d6d6d 70%, var(--photo-light) 100%);
  }
  .shapes { position: absolute; inset: 0; }
  .pain-questions {
    position: absolute; top: 30px; left: 0; width: 855px;
    display: flex; justify-content: space-between; padding: 0 30px 0 34px;
    color: var(--white); font-weight: 700; font-size: 34px; letter-spacing: 0.3px;
  }
  .title {
    position: absolute; top: 112px; left: 64px; width: 724px;
    text-align: center; color: var(--white); line-height: 1.08;
  }
  .title-light { display: block; font-weight: 400; font-size: 62px; }
  .title-bold { display: block; font-weight: 700; font-size: 64px; }
  .booking {
    position: absolute; top: 290px; left: 170px; width: 480px;
    text-align: center; color: var(--white); font-weight: 700;
  }
  .booking-note { font-size: 19px; line-height: 28px; }
  .booking-note.small { font-size: 16.5px; }
  .event-time { margin-top: 10px; font-size: 31px; line-height: 37px; }
  .event-time sup { font-size: 18px; }
  .topics {
    position: absolute; top: 588px; left: 203px; width: 476px; height: 180px;
    background: var(--panel); padding: 22px 0 0 30px;
    list-style: none; color: var(--white); font-weight: 700; font-size: 22px; line-height: 31px;
  }
  .topics li::before { content: "•"; margin-right: 8px; font-size: 18px; }
  .speaker-photo { position: absolute; }
  .speaker-name {
    position: absolute; top: 966px; width: 140px; text-align: center;
    font-size: 13px; color: var(--ink); line-height: 17px;
  }
  .speaker-name strong { font-weight: 700; }
  .brand-box {
    position: absolute; top: 1016px; left: 264px; width: 330px; height: 108px;
    border: 5px solid #111; border-radius: 10px; background: #f4f4f4;
    display: flex; align-items: center; justify-content: center;
    font-weight: 800; font-size: 38px; color: var(--blue); letter-spacing: 1px;
  }
  .address {
    position: absolute; top: 1133px; left: 0; width: 855px; text-align: center;
    font-weight: 700; font-size: 13.5px; color: var(--ink);
  }
  .website {
    position: absolute; top: 1156px; left: 0; width: 855px; text-align: center;
    font-weight: 700; font-size: 25px; color: var(--ink);
  }
</style>
</head>
<body>
<main class="flyer">
  <div class="hero-photo" role="img" aria-label="Black and white photo of hands pressing on a sore lower back"></div>

  <svg class="shapes" width="855" height="1200" viewBox="0 0 855 1200">
    <!-- top band -->
    <path d="M0 0 H855 V98 Q427 150 0 98 Z" fill="var(--blue)"/>
    <!-- ribbon folds -->
    <polygon points="64,274 201,276 182,300" fill="var(--brown-fold)"/>
    <polygon points="788,274 650,276 668,300" fill="var(--brown-fold)"/>
    <!-- orange pointer -->
    <polygon points="201,274 652,274 630,467 480,467 394,572 326,467 167,467" fill="var(--orange)"/>
    <!-- brown ribbon -->
    <polygon points="92,93 760,93 788,274 64,274" fill="var(--brown-dark)"/>
    <!-- bottom panel -->
    <path d="M0 975 Q427 780 855 985 V1200 H0 Z" fill="var(--blue)"/>
    <path d="M0 990 Q427 800 855 1000 V1200 H0 Z" fill="#ececec"/>
    <!-- speaker shadows -->
    <ellipse cx="347" cy="953" rx="62" ry="7" fill="#777"/>
    <ellipse cx="506" cy="953" rx="62" ry="7" fill="#777"/>
    <!-- speaker portraits -->
    <g role="img" aria-label="Headshot of speaker Daniel Marsh">
      <circle cx="347" cy="891" r="69" fill="#9a8a6e" stroke="var(--orange)" stroke-width="5"/>
    </g>
    <g role="img" aria-label="Headshot of speaker Carter Holloway">
      <circle cx="506" cy="891" r="69" fill="#b58a6a" stroke="var(--orange)" stroke-width="5"/>
    </g>
  </svg>

  <header class="pain-questions">
    <span>BACK PAIN?</span><span>SHOULDER PAIN?</span><span>KNEE PAIN?</span>
  </header>

  <h1 class="title">
    <span class="title-light">FREE SEMINAR ON</span>
    <span class="title-bold">HOW TO STOP PAIN</span>
  </h1>

  <section class="booking">
    <p class="booking-note">RESERVATIONS REQUIRED.</p>
    <p class="booking-note">CALL 303-555-0142 TODAY</p>
    <p class="booking-note small">LIMITED SPACE SO DON’T WAIT TO SIGN UP</p>
    <p class="event-time">THURSDAY, APRIL 13<sup>th</sup><br>7:30PM - 9:00PM</p>
  </section>

  <ul class="topics">
    <li>How to Get Out of Pain</li>
    <li>What to do When an Exercise Hurts</li>
    <li>How Exercise Helps Pain</li>
    <li>Q &amp; A to Fine Extraordinary Health</li>
  </ul>

  <p class="speaker-name" style="left:277px"><strong>Daniel Marsh,</strong><br>PT, DPT, OCS</p>
  <p class="speaker-name" style="left:436px"><strong>Carter Holloway,</strong><br>MS, CSCS, FMS</p>

  <div class="brand-box">STRIDELINE</div>

  <p class="address">STRIDELINE PERSONAL TRAINING STUDIO 214 Elm St. Fairview, CO 80000</p>
  <p class="website">www.Stridelinefit.com</p>
</main>
</body>
</html>
```